Funky Cup design on our hot disposable cups

I would like two examples: one orange cup (like our logo color) with white writing, one white cup with orange writing:
On the top: Organic coffee because we care
Middle: Our logo (attached but drop the R in the circle)
Bottom: Live Life Like a Tinker
Would love ideas what else can be written or patterned around the cup, clever design such as Coffee moorings or any other funky ideas.

It should include the text "tinkers & tide " all over the cup around the logo!

thanks.

Target Market(s)

female and male 17 to 30s

Industry/Entity Type

Coffee

Font styles to use
Other font styles liked:
• Galano grotesque like our logosame as logo

Colors
EE7325
F08F49
F5BC92
FAE3D3
FDF4ED

Requirements
Must have
• cool fun , trendy look. It should include the text "tinkers & tide " all over the cup around the logo!
Should not have
• in my logo please drop the r with the circle

```html
<!DOCTYPE html>
<html lang="en">
<head>
<meta charset="utf-8">
<title>tinkers &amp; tide — Cup Wrap</title>
<link rel="stylesheet" href="https://fonts.googleapis.com/css2?family=Lobster&family=Libre+Baskerville&family=Outfit:wght@600;700&display=swap">
<style>
  :root {
    --orange: #eb6b2a;
    --orange-soft: #f08f49;
    --white: #f7f6f5;
    --backdrop: #e4e4e4;
  }
  html, body {
    margin: 0;
    width: 1200px;
    height: 1068px;
    overflow: hidden;
    background: var(--backdrop);
  }
  .cup-wrap {
    position: absolute;
    left: 250px;
    top: 84px;
    width: 700px;
    height: 900px;
    overflow: hidden;
  }
  .cup-wrap svg { position: absolute; inset: 0; }
  .label-text {
    position: absolute;
    left: 0;
    width: 700px;
    text-align: center;
    color: var(--orange);
    white-space: nowrap;
  }
  .organic {
    top: 78px;
    font-family: "Lobster", cursive;
    font-size: 44px;
    line-height: 1;
    transform: rotate(-5deg);
  }
  .coffee {
    top: 134px;
    font-family: "Libre Baskerville", serif;
    font-size: 44px;
    line-height: 1;
  }
  .care {
    top: 196px;
  }
  .care span {
    display: inline-block;
    background: var(--orange);
    color: var(--white);
    font-family: "Outfit", sans-serif;
    font-weight: 600;
    font-size: 14px;
    letter-spacing: 1px;
    padding: 3px 10px;
  }
  .brand-name {
    top: 500px;
    font-family: "Outfit", sans-serif;
    font-weight: 700;
    font-size: 44px;
    line-height: 1.05;
  }
  .tagline {
    top: 776px;
    font-family: "Outfit", sans-serif;
    font-weight: 700;
    font-size: 30px;
    line-height: 1.2;
  }
  .tagline-rule {
    position: absolute;
    left: 326px;
    top: 860px;
    width: 48px;
    height: 4px;
    background: var(--orange);
  }
</style>
</head>
<body>
  <div class="cup-wrap">
    <svg width="700" height="900" viewBox="0 0 700 900">
      <rect class="doodle-field" x="0" y="0" width="700" height="900" fill="var(--orange)" role="img" aria-label="Faint line-drawn coffee doodle pattern on orange"/>
      <path class="band-outer-line" d="M196,-10 V391.4 A214,214 0 0 0 196,688.6 V910 H504 V688.6 A214,214 0 0 0 504,391.4 V-10 Z" fill="none" stroke="var(--white)" stroke-width="4"/>
      <path class="label-band" d="M210,-10 V398.6 A200,200 0 0 0 210,681.4 V910 H490 V681.4 A200,200 0 0 0 490,398.6 V-10 Z" fill="var(--white)"/>
      <path class="band-inner-line" d="M224,-10 V403.2 A186,186 0 0 0 224,676.8 V910 M476,-10 V403.2 A186,186 0 0 1 476,676.8 V910" fill="none" stroke="var(--orange)" stroke-width="4"/>
      <circle class="brand-dot" cx="350" cy="440" r="22" fill="var(--orange)"/>
    </svg>
    <div class="label-text organic">Organic</div>
    <div class="label-text coffee">COFFEE</div>
    <div class="label-text care"><span>BECAUSE WE CARE</span></div>
    <div class="label-text brand-name">tinkers<br>&amp; tide</div>
    <div class="label-text tagline">Live Life<br>Like a Tinker</div>
    <div class="tagline-rule"></div>
  </div>
</body>
</html>
```